Design business card for new business which advocates for elders in nursing homes or personal care h

New business for rights of the elderly residents who reside in personal care homes and or nursing homes. I am looking for a business card with logo of keystone for Pennsylvania and something in side the keystone that represents healthcare, advocates, something on that line; monitor care received and needs of resident. Chart audits, State Regulation compliance

Target Market(s)

Seniors no longer safe to live at home by themselves along with their kids

Industry/Entity Type

Business

Contact Information for Business Card

Keystone symbol to represent Pensylvaoa with some kind of symbol inside to represent advocate, seniors, or healthcare symbol

Font styles to use
Serif

Colors
33a6d7
85cae6
abd037

Requirements
Must have
• Brightwell Elder Allies is our business name; our tag line is Path to Better Living
Nice to have
• Nice logo

```html
<!DOCTYPE html>
<html lang="en">
<head>
<meta charset="utf-8">
<title>Brightwell Elder Allies – Business Card</title>
<link href="https://fonts.googleapis.com/css2?family=Jura:wght@400;500;600&display=swap" rel="stylesheet">
<style>
  :root {
    --blue: #33a6d7;
    --blue-light: #85cae6;
    --green: #abd037;
    --orange: #f0892e;
    --ink: #2a2a2a;
    --paper: #ffffff;
    --border: #d9d9d9;
  }
  * { margin: 0; padding: 0; box-sizing: border-box; }
  html, body { width: 849px; height: 1200px; overflow: hidden; background: var(--paper); }
  body { position: relative; font-family: "Jura", sans-serif; color: var(--ink); }

  .card {
    position: absolute; left: 119px; width: 611px; height: 348px;
    background: var(--paper); border: 1px solid var(--border); overflow: hidden;
  }
  .card--front { top: 175px; }
  .card--back { top: 580px; }
  .card svg.swoosh { position: absolute; inset: 0; width: 100%; height: 100%; }

  .brand-mark {
    position: absolute; width: 46px; height: 46px; border-radius: 50%;
    background: var(--orange);
  }
  .brand-name {
    position: absolute; color: var(--blue); font-weight: 500; white-space: nowrap;
    text-align: center;
  }
  .brand-rule { position: absolute; height: 2px; background: var(--blue-light); }
  .brand-tagline { position: absolute; color: var(--ink); white-space: nowrap; text-align: center; font-weight: 500; }

  /* front */
  .card--front .brand-mark { left: 282px; top: 84px; width: 48px; height: 48px; }
  .card--front .brand-name { left: 0; width: 611px; top: 186px; font-size: 30px; }
  .card--front .brand-rule { left: 160px; width: 292px; top: 232px; }
  .card--front .brand-tagline { left: 0; width: 611px; top: 240px; font-size: 20px; }

  /* back */
  .card--back .brand-mark { left: 154px; top: 116px; width: 38px; height: 38px; }
  .card--back .brand-name { left: 16px; width: 316px; top: 174px; font-size: 21px; }
  .card--back .brand-rule { left: 28px; width: 292px; top: 204px; height: 1.5px; }
  .card--back .brand-tagline { left: 16px; width: 316px; top: 212px; font-size: 14px; }

  .person { position: absolute; right: 34px; top: 92px; text-align: right; }
  .person__name { font-size: 24px; font-weight: 500; }
  .person__role { font-size: 13px; margin-top: 6px; }

  .contact { position: absolute; right: 34px; top: 192px; text-align: right; font-size: 16px; line-height: 25px; font-weight: 500; }
  .address { position: absolute; right: 30px; top: 302px; font-size: 16px; font-weight: 500; }
</style>
</head>
<body>

<section class="card card--front" aria-label="Card front">
  <svg class="swoosh" viewBox="0 0 611 348" preserveAspectRatio="none" aria-hidden="true">
    <path d="M250 0 L611 0 L611 95 C540 40 420 10 250 0 Z" fill="var(--green)"/>
    <path d="M0 262 C180 300 420 300 611 250 L611 348 L0 348 Z" fill="var(--blue)"/>
    <path d="M0 262 C180 300 420 300 611 250 L611 270 C420 315 180 312 0 285 Z" fill="var(--blue-light)"/>
  </svg>
  <div class="brand-mark"></div>
  <div class="brand-name">Brightwell Elder Allies</div>
  <div class="brand-rule"></div>
  <div class="brand-tagline">Path to Better Living</div>
</section>

<section class="card card--back" aria-label="Card back">
  <svg class="swoosh" viewBox="0 0 611 348" preserveAspectRatio="none" aria-hidden="true">
    <path d="M0 0 L330 0 C220 10 90 45 0 105 Z" fill="var(--green)"/>
    <path d="M611 200 C560 250 470 300 330 348 L611 348 Z" fill="var(--blue-light)"/>
    <path d="M611 255 C570 290 520 320 470 348 L611 348 Z" fill="var(--blue)"/>
  </svg>
  <div class="brand-mark"></div>
  <div class="brand-name">Brightwell Elder Allies</div>
  <div class="brand-rule"></div>
  <div class="brand-tagline">Path to Better Living</div>

  <div class="person">
    <div class="person__name">Daniel Harper</div>
    <div class="person__role">Advocate</div>
  </div>
  <div class="contact">
    <div>Call:-+61 2045 1873</div>
    <div>hello@brightwell.com</div>
    <div>www.brightwell.com</div>
  </div>
  <div class="address">Maple St 48, Oak Park, Sydney</div>
</section>

</body>
</html>
```